Business card for utility of the future

I need a business card template designed for brookvane. We provide sustainable water, energy and waste services to homes.

The card should include name, position, email address, phone number, website and our logo (attached). I would like it to convey professionalism and creativity.

Target Market(s)

Homeowners, investors, corporate partners.

Industry/Entity Type

Utility

Contact Information for Business Card

The card should include name, position, email address, phone number, website and our logo (attached).

```html
<!DOCTYPE html>
<html lang="en">
<head>
<meta charset="utf-8">
<title>brookvane business card</title>
<link rel="stylesheet" href="https://fonts.googleapis.com/css2?family=Lato:wght@400;700;900&display=swap">
<style>
  :root {
    --green: #4fb072;
    --green-soft: #6cc08a;
    --orange: #d8744e;
    --ink: #2b2b2b;
    --grey: #6b6b6b;
    --paper: #f7f7f7;
    --backdrop: #3a3a3a;
  }
  * { box-sizing: border-box; margin: 0; padding: 0; }
  html, body { width: 1200px; height: 873px; overflow: hidden; }
  body {
    background: var(--backdrop);
    font-family: "Lato", Arial, sans-serif;
    position: relative;
  }
  .card {
    position: absolute;
    width: 560px;
    height: 320px;
    border-radius: 4px;
    overflow: hidden;
    box-shadow: 0 10px 30px rgba(0,0,0,.45);
  }
  /* back side */
  .card-back {
    left: 60px; top: 60px;
    background: var(--green-soft);
  }
  .card-back .wordmark {
    position: absolute;
    left: 0; right: 0; top: 110px;
    text-align: center;
    color: #fff;
    font-weight: 900;
    font-size: 72px;
    line-height: 1;
    letter-spacing: -1px;
  }
  .card-back .website {
    position: absolute;
    left: 0; right: 0; bottom: 46px;
    text-align: center;
    color: #fff;
    font-size: 12px;
    letter-spacing: 4px;
    opacity: .9;
  }
  /* front side */
  .card-front {
    left: 580px; top: 440px;
    background: var(--paper);
  }
  .card-front .wordmark {
    position: absolute;
    left: 0; right: 40px; top: 50px;
    text-align: center;
    color: var(--green);
    font-weight: 900;
    font-size: 60px;
    line-height: 1;
    letter-spacing: -1px;
  }
  .holder {
    position: absolute;
    right: 34px; top: 138px;
    text-align: right;
  }
  .holder-name {
    color: var(--green);
    font-weight: 900;
    font-size: 19px;
    letter-spacing: .3px;
  }
  .holder-role {
    color: var(--grey);
    font-size: 12px;
    margin-top: 2px;
  }
  .icon-tab {
    position: absolute;
    left: 0; top: 168px;
    width: 46px; height: 118px;
    background: var(--green);
    border-radius: 0 12px 12px 0;
    display: flex;
    flex-direction: column;
    justify-content: space-around;
    align-items: center;
    padding: 8px 0;
  }
  .icon-tab svg { width: 18px; height: 18px; }
  .contact {
    position: absolute;
    left: 62px; top: 180px;
    list-style: none;
    color: var(--ink);
    font-size: 15px;
    font-weight: 700;
  }
  .contact li { height: 30px; line-height: 30px; white-space: nowrap; }
  .band {
    position: absolute;
    bottom: 0;
    height: 16px;
  }
  .band-green { left: 0; width: 380px; background: var(--green); }
  .band-orange {
    right: 0; width: 190px; height: 22px;
    background: var(--orange);
    border-radius: 22px 0 0 0;
  }
</style>
</head>
<body>

<section class="card card-back">
  <div class="wordmark">brookvane</div>
  <div class="website">www.brookvane.com</div>
</section>

<section class="card card-front">
  <div class="wordmark">brookvane</div>

  <div class="holder">
    <div class="holder-name">DANIEL MORENO</div>
    <div class="holder-role">CTO &amp; Executive VP</div>
  </div>

  <div class="icon-tab">
    <svg viewBox="0 0 24 24" aria-label="phone"><path fill="#fff" d="M6.6 10.8a15 15 0 0 0 6.6 6.6l2.2-2.2c.3-.3.7-.4 1-.2 1.1.4 2.3.6 3.6.6.6 0 1 .4 1 1V20c0 .6-.4 1-1 1A17 17 0 0 1 3 4c0-.6.4-1 1-1h3.5c.6 0 1 .4 1 1 0 1.3.2 2.5.6 3.6.1.3 0 .7-.2 1z"/></svg>
    <svg viewBox="0 0 24 24" aria-label="email"><rect x="3" y="5" width="18" height="14" rx="1" fill="none" stroke="#fff" stroke-width="2"/><path d="M3 6l9 7 9-7" fill="none" stroke="#fff" stroke-width="2"/></svg>
    <svg viewBox="0 0 24 24" aria-label="link"><path d="M10 14a4 4 0 0 0 5.7 0l3-3a4 4 0 0 0-5.7-5.7l-1.2 1.2M14 10a4 4 0 0 0-5.7 0l-3 3a4 4 0 0 0 5.7 5.7l1.2-1.2" fill="none" stroke="#fff" stroke-width="2" stroke-linecap="round"/></svg>
  </div>

  <ul class="contact">
    <li>+1 (949) 555-0142</li>
    <li>daniel.m@brookvane.com</li>
    <li>4120 Larkin Ave, Irvine, CA 92606</li>
  </ul>

  <div class="band band-green"></div>
  <div class="band band-orange"></div>
</section>

</body>
</html>
```